Label Design for an exciting food startup introducing millets to North America!

We need a label for Millet grains (and millet flour after design is finalized for the grains because it will be very similar except for the description) Looking for a clean, minimalistic design. Modern feel. We are a social enterprise introducing millet based products to North American Market and we cater to the customers who are health conscious, eat plant-based foods, may have gluten allergies and are looking for a healthy substitutes for carbohydrate-rich foods.Millets are a great alternative for rice/barley/couscous/quinoa. Very nutritious grain!Our big audacious goal is to make Millets the new Quinoa in the next 3 years!!! More information about the company can be found on the website koshafoods.comMore information in the brief attached.

Target Market(s)

Women (75%) and men (25%) aged 21-60 who are health conscious, want to eat vegan/plant based foods, willing to experiment with new foods. They care about the environment and doing good while choosing products that are good for them and the planet.

Industry/Entity Type

Food Production

Colors

Designer to choose colors to be used in the design.

Requirements
Must have
• Covered in the project brief attached
Nice to have
Should not have

```html
<!DOCTYPE html>
<html lang="en">
<head>
<meta charset="utf-8">
<title>Ravelun Foods – Millet Grains Label</title>
<link rel="stylesheet" href="https://fonts.googleapis.com/css2?family=Amatic+SC:wght@700&family=Delius&family=Patrick+Hand&display=swap">
<style>
  :root {
    --bg: #ececec;
    --paper: #ffffff;
    --magenta: #c2237e;
    --orange: #ea5a2e;
    --lime: #c9dc4a;
    --purple: #8c2b86;
    --leaf-green: #a9c93c;
    --leaf-orange: #ec6b3a;
    --title: #c7703a;
    --brand: #b5693a;
    --grain: #b7a540;
    --swash: #e4e47a;
    --ink-dark: #4a4a3a;
  }
  * { margin: 0; padding: 0; box-sizing: border-box; }
  html, body { width: 1160px; height: 1200px; overflow: hidden; background: var(--bg); }
  .canvas { position: relative; width: 1160px; height: 1200px; }

  .pouch {
    position: absolute; left: 260px; top: 40px; width: 640px; height: 1120px;
    background: var(--paper); border-radius: 14px; overflow: hidden;
    box-shadow: 0 4px 18px rgba(0,0,0,0.08);
  }
  .pattern-band {
    position: absolute; left: 0; top: 0; width: 640px; height: 640px;
    background: linear-gradient(90deg, var(--magenta) 0%, var(--magenta) 22%, var(--orange) 24%, var(--orange) 76%, var(--lime) 78%, var(--lime) 100%);
  }
  .pattern-band::after {
    content: ""; position: absolute; inset: 0;
    background: radial-gradient(circle at 50% 30%, rgba(140,43,134,0.35), rgba(140,43,134,0) 60%);
  }
  .grain-window {
    position: absolute; left: 0; top: 640px; width: 640px; height: 178px;
    background: linear-gradient(180deg, #a8963a, var(--grain) 40%, #c3b255);
  }
  .dish-photo {
    position: absolute; left: 36px; top: 818px; width: 320px; height: 268px;
    border-radius: 0 0 160px 160px / 0 0 90px 90px;
    background: radial-gradient(ellipse at 45% 45%, #e0803a 0%, #c7a07a 45%, #6b4a2e 80%, #ffffff 100%);
  }

  .seal {
    position: absolute; left: 147px; top: 258px; width: 350px; height: 350px;
    border-radius: 50%; background: var(--paper); border: 12px solid var(--purple);
    text-align: center; z-index: 1;
  }
  .seal-line {
    display: flex; align-items: center; justify-content: center; gap: 18px;
    margin-top: 48px; font-family: "Patrick Hand", cursive; font-size: 26px;
    letter-spacing: 2px; color: var(--brand);
  }
  .seal-dot { width: 28px; height: 28px; border-radius: 50%; background: var(--leaf-orange); }
  .brand-name { font-family: "Delius", sans-serif; font-size: 21px; color: var(--brand); margin-top: 12px; }
  .product-title {
    font-family: "Amatic SC", sans-serif; font-weight: 700; color: var(--title);
    font-size: 98px; line-height: 0.86; margin-top: 8px; letter-spacing: 2px;
  }

  .claim-leaf { position: absolute; z-index: 2; overflow: visible; }
  .claim-leaf text { font-family: "Patrick Hand", cursive; }

  .diet-tag {
    position: absolute; left: 372px; top: 905px; width: 240px; height: 100px; text-align: center;
    white-space: nowrap;
  }
  .diet-swash {
    position: absolute; left: 20px; top: 14px; width: 200px; height: 78px;
    background: var(--swash); border-radius: 40px 10px 40px 10px; transform: rotate(-4deg);
  }
  .diet-main {
    position: relative; font-family: "Patrick Hand", cursive; font-size: 34px;
    letter-spacing: 3px; color: var(--ink-dark); transform: rotate(-4deg);
  }
  .diet-sub {
    position: relative; font-family: "Patrick Hand", cursive; font-size: 22px;
    letter-spacing: 1px; color: var(--ink-dark); margin-top: 4px; transform: rotate(-4deg);
  }
</style>
</head>
<body>
<div class="canvas">
  <div class="pouch">
    <div class="pattern-band" role="img" aria-label="Decorative pattern of large stylised flowers and leaves in magenta, orange, lime and purple"></div>

    <svg class="claim-leaf" style="left:14px;top:252px" width="175" height="145" viewBox="0 0 175 145">
      <path d="M10 20 C70 0 150 40 162 128 C90 132 18 92 10 20 Z" fill="var(--leaf-green)" stroke="#fff" stroke-width="4"/>
      <text x="40" y="37" font-size="14" fill="var(--purple)" transform="rotate(35 40 37)">Low Glycemic Index</text>
      <text x="39" y="58" font-size="14" fill="var(--purple)" transform="rotate(35 39 58)">Diabetic Friendly</text>
    </svg>

    <svg class="claim-leaf" style="left:380px;top:160px" width="200" height="130" viewBox="0 0 200 130">
      <path d="M10 115 C30 40 110 5 190 15 C175 85 100 125 10 115 Z" fill="var(--leaf-orange)" stroke="#fff" stroke-width="4"/>
      <text x="45" y="85" font-size="15" fill="#fbe7c8" transform="rotate(-28 45 85)">Source of Protein,</text>
      <text x="58" y="102" font-size="15" fill="#fbe7c8" transform="rotate(-28 58 102)">Fibre and Minerals</text>
    </svg>

    <div class="seal">
      <div class="seal-line"><span>WHOLE</span><span class="seal-dot"></span><span>GRAIN</span></div>
      <div class="brand-name">Ravelun Foods</div>
      <div class="product-title">MILLET<br>GRAINS</div>
    </div>

    <div class="grain-window" role="img" aria-label="Clear window showing the golden millet grains inside"></div>
    <div class="dish-photo" role="img" aria-label="Photo of a wooden bowl of cooked millet salad with diced carrot, beetroot and green onion"></div>

    <div class="diet-tag">
      <div class="diet-swash"></div>
      <div class="diet-main">· RAW VEGAN ·</div>
      <div class="diet-sub">GLUTEN-FREE</div>
    </div>
  </div>
</div>
</body>
</html>
```